Velo Mirth is a high end dessert topping line made with all natural ingredients and no preservatives. The initial flavor is fudge with more flavors to follow such as peppermint, salted caamel etc. My target market will be specialty food stores. I will be selling my product in 9 oz and 4 oz straight sided jars. I am open to all ideas but am leaning toward a more upscale, sophisticated look with colors/design that will stand out on a shelf. I want the flavor of the topping to feature prominently in the design so the product is readily identifiable to the consumer. I also need room for nutritional facts.

```html
<!DOCTYPE html>
<html lang="en">
<head>
<meta charset="utf-8">
<title>Velo Mirth – Hot Fudge Label</title>
<link rel="stylesheet" href="https://fonts.googleapis.com/css2?family=Oswald:wght@400&family=Jost:wght@500;600&display=swap">
<style>
  :root {
    --paper: #ffffff;
    --cocoa: #846c50;
    --gold: #d2c07a;
    --ink: #0a0a0a;
    --cream: #ffffff;
  }
  html, body {
    margin: 0;
    padding: 0;
    width: 1200px;
    height: 1000px;
    overflow: hidden;
    background: var(--paper);
  }
  .canvas {
    position: relative;
    width: 1200px;
    height: 1000px;
  }
  .label {
    position: absolute;
    left: 434px;
    top: 284px;
    width: 332px;
    height: 433px;
  }
  .label-pattern {
    position: absolute;
    inset: 0;
    background: linear-gradient(90deg, var(--cocoa) 0%, #9a8558 50%, var(--cocoa) 100%);
  }
  .brand-panel {
    position: absolute;
    left: 42px;
    top: 47px;
    width: 248px;
    height: 234px;
    background: var(--gold);
    text-align: center;
  }
  .brand-mark {
    position: absolute;
    left: 50%;
    top: 30px;
    width: 56px;
    height: 56px;
    margin-left: -28px;
    border-radius: 50%;
    background: var(--cocoa);
  }
  .brand-name {
    position: absolute;
    left: 0;
    right: 0;
    top: 116px;
    margin: 0;
    font-family: "Oswald", sans-serif;
    font-weight: 400;
    font-size: 50px;
    line-height: 1.1;
    letter-spacing: 0;
    white-space: nowrap;
    color: var(--ink);
  }
  .brand-tagline {
    position: absolute;
    left: 0;
    right: 0;
    top: 203px;
    margin: 0;
    font-family: "Jost", sans-serif;
    font-weight: 600;
    font-size: 11.5px;
    letter-spacing: 0.4px;
    white-space: nowrap;
    color: var(--ink);
  }
  .flavor-band {
    position: absolute;
    left: 42px;
    top: 303px;
    width: 247px;
    height: 80px;
    background: var(--ink);
    display: flex;
    align-items: center;
    justify-content: center;
  }
  .flavor-name {
    margin: 0;
    font-family: "Jost", sans-serif;
    font-weight: 500;
    font-size: 22px;
    letter-spacing: 4px;
    white-space: nowrap;
    color: var(--cream);
  }
</style>
</head>
<body>
  <main class="canvas">
    <section class="label">
      <div class="label-pattern" role="img" aria-label="Vertical wavy stripes in cocoa brown, gold and black"></div>
      <div class="brand-panel">
        <span class="brand-mark" aria-hidden="true"></span>
        <h1 class="brand-name">VELO MIRTH</h1>
        <p class="brand-tagline">GOURMET DESSERT TOPPING</p>
      </div>
      <div class="flavor-band">
        <h2 class="flavor-name">HOT FUDGE</h2>
      </div>
    </section>
  </main>
</body>
</html>
```